Copper Wagon
ideas, energy & innovation
Can you also please upload drafts of the letter headed paper, compliments slips and invoice drafts for me to also look at!

```html
<!DOCTYPE html>
<html lang="en">
<head>
<meta charset="utf-8">
<title>Copper Wagon – Business Card</title>
<link href="https://fonts.googleapis.com/css2?family=Open+Sans:wght@400;600;700&display=swap" rel="stylesheet">
<style>
  :root {
    --backdrop: #e6e6e6;
    --card: #ffffff;
    --ink: #3b3b3b;
    --ink-soft: #555555;
    --brand-blue: #1f4c9e;
    --brand-blue-deep: #163a80;
    --brand-green: #7cb82f;
    --rule: #cfcfcf;
  }
  * { box-sizing: border-box; margin: 0; padding: 0; }
  html, body {
    width: 1200px; height: 780px; overflow: hidden;
    background: var(--backdrop);
    font-family: "Open Sans", Arial, sans-serif;
    color: var(--ink);
  }
  .business-card {
    position: absolute; left: 120px; top: 100px;
    width: 960px; height: 580px;
    background: var(--card);
    border-radius: 32px;
    overflow: hidden;
    box-shadow: 0 6px 18px rgba(0,0,0,0.15);
  }
  .edge-swoosh { position: absolute; left: 0; top: 0; width: 960px; height: 580px; }
  .brand {
    position: absolute; left: 128px; top: 128px;
    display: flex; align-items: center; gap: 22px;
  }
  .brand-dot {
    width: 78px; height: 78px; border-radius: 50%;
    background: var(--brand-blue);
  }
  .brand-name {
    font-size: 58px; font-weight: 600; color: var(--ink);
    letter-spacing: -0.5px;
  }
  .person {
    position: absolute; right: 560px; top: 292px; text-align: right;
  }
  .person-name { font-size: 30px; font-weight: 700; color: var(--brand-blue); line-height: 1.2; }
  .person-role { font-size: 22px; font-weight: 700; color: var(--brand-green); line-height: 1.3; }
  .address {
    position: absolute; right: 560px; top: 402px; text-align: right;
    font-size: 20px; line-height: 1.55; color: var(--ink-soft);
  }
  .divider {
    position: absolute; left: 430px; top: 288px; width: 1px; height: 236px;
    background: var(--rule);
  }
  .contact-list {
    position: absolute; left: 458px; top: 284px; list-style: none;
    font-size: 20px; color: var(--ink-soft); line-height: 1;
  }
  .contact-list li { display: flex; align-items: center; height: 33px; }
  .contact-icon { width: 24px; height: 24px; margin-right: 10px; flex: none; color: var(--brand-blue); }
  .contact-list .licence { padding-left: 34px; }
</style>
</head>
<body>
  <div class="business-card">
    <svg class="edge-swoosh" viewBox="0 0 960 580" aria-hidden="true">
      <defs>
        <linearGradient id="band-blue" x1="0" y1="0" x2="1" y2="1">
          <stop offset="0" stop-color="#2c62b8"/>
          <stop offset="1" stop-color="#163a80"/>
        </linearGradient>
      </defs>
      <path d="M0,150 C28,300 52,470 132,580 L0,580 Z" fill="url(#band-blue)"/>
      <path d="M0,120 C42,290 78,470 178,590" fill="none" stroke="var(--brand-green)" stroke-width="7"/>
    </svg>

    <div class="brand">
      <span class="brand-dot"></span>
      <span class="brand-name">CopperWagon</span>
    </div>

    <div class="person">
      <p class="person-name">Rosa Penhallow</p>
      <p class="person-role">Director</p>
    </div>

    <p class="address">14 Larchmont Street,<br>Ferndale, Victoria. 3198</p>

    <div class="divider"></div>

    <ul class="contact-list">
      <li>
        <svg class="contact-icon" viewBox="0 0 24 24"><path d="M6 3l3 0 1.5 4.5-2 1.5a11 11 0 0 0 6.5 6.5l1.5-2 4.5 1.5 0 3c0 1-1 2-2 2C10 20 4 14 4 5c0-1 1-2 2-2z" fill="currentColor"/></svg>
        03 9412 5086
      </li>
      <li>
        <svg class="contact-icon" viewBox="0 0 24 24"><rect x="7" y="2" width="10" height="20" rx="2" fill="currentColor"/><rect x="9" y="5" width="6" height="10" fill="#fff"/><circle cx="12" cy="18.5" r="1.2" fill="#fff"/></svg>
        0431 208 774
      </li>
      <li>
        <svg class="contact-icon" viewBox="0 0 24 24"><text x="12" y="19" text-anchor="middle" font-family="Open Sans, Arial, sans-serif" font-size="22" font-weight="700" fill="currentColor">@</text></svg>
        rosa@copperwagon.com.au
      </li>
      <li>
        <svg class="contact-icon" viewBox="0 0 24 24"><circle cx="12" cy="12" r="9" fill="none" stroke="currentColor" stroke-width="2"/><ellipse cx="12" cy="12" rx="4" ry="9" fill="none" stroke="currentColor" stroke-width="1.5"/><line x1="3" y1="12" x2="21" y2="12" stroke="currentColor" stroke-width="1.5"/></svg>
        www.copperwagon.com.au
      </li>
      <li class="licence">Lic.no : ABN 47 615 903 218</li>
    </ul>
  </div>
</body>
</html>
```